Complete Banner Set For Web Display Ads - Including Zimbly

Ads are driving to a free web class on real estate investing made easy. The offer is for software and training that solves their number 1 challenge - Finding Deals.
Examples of copy suggestions and offer....
"Invest In Real Estate Like A Pro"
"Access Never Before Seen Inventory In Seconds"
"The Country's Best Source For Off-Market Deals"
Brody Halvaney "#1 Real Estate Investing Strategy"
Real Estate

```html
<!DOCTYPE html>
<html lang="en">
<head>
<meta charset="utf-8">
<title>Banner Set – Invest in Real Estate Like a PRO</title>
<link rel="stylesheet" href="https://fonts.googleapis.com/css2?family=Arimo:wght@400;700&display=swap">
<style>
  :root {
    --canvas: #ffffff;
    --sky-top: #1ba6d3;
    --sky-bottom: #0d7399;
    --leaf: #5cb531;
    --leaf-light: #e9f7dc;
    --paper: #ffffff;
    --ink: #1c2536;
    --night: #283647;
    --cta-top: #f4603f;
    --cta-bottom: #d8361c;
    --cta-edge: #b42a14;
    --label: #333333;
    --frame: #8a939c;
    --photo-light: #ece3dc;
    --photo-mid: #b9a293;
    --photo-dark: #4d5d7a;
  }
  * { margin: 0; padding: 0; box-sizing: border-box; }
  html, body { width: 1200px; height: 1200px; overflow: hidden; }
  body {
    background: var(--canvas);
    font-family: "Arimo", Arial, sans-serif;
    position: relative;
  }
  .banner {
    position: absolute;
    overflow: hidden;
    border: 1px solid var(--frame);
    background: var(--paper);
  }
  .band-sky {
    position: absolute;
    background: linear-gradient(180deg, var(--sky-top) 0%, var(--sky-top) 45%, var(--sky-bottom) 100%);
  }
  .band-leaf-h {
    position: absolute;
    background: linear-gradient(90deg, var(--leaf) 0%, var(--leaf) 30%, var(--leaf-light) 50%, var(--leaf) 70%, var(--leaf) 100%);
  }
  .band-leaf-v {
    position: absolute;
    background: linear-gradient(180deg, var(--leaf) 0%, var(--leaf) 30%, var(--leaf-light) 50%, var(--leaf) 70%, var(--leaf) 100%);
  }
  .band-night { position: absolute; background: var(--night); }
  .headline {
    position: absolute;
    color: #fff;
    font-weight: 700;
    white-space: nowrap;
    text-shadow: 0 1px 2px rgba(0,0,0,.35);
  }
  .tagline {
    position: absolute;
    color: var(--ink);
    font-weight: 700;
    white-space: nowrap;
  }
  .portrait {
    position: absolute;
    background:
      radial-gradient(ellipse 38% 30% at 50% 32%, var(--photo-mid) 0%, var(--photo-mid) 60%, transparent 62%),
      linear-gradient(180deg, var(--photo-light) 0%, var(--photo-light) 55%, var(--photo-dark) 75%, var(--photo-dark) 100%);
  }
  .cta {
    position: absolute;
    width: 153px;
    height: 42px;
    border-radius: 4px;
    border: 1px solid var(--cta-edge);
    background: linear-gradient(180deg, var(--cta-top) 0%, var(--cta-bottom) 100%);
    color: #fff;
    font-weight: 700;
    font-size: 19px;
    line-height: 40px;
    text-align: center;
    text-shadow: 0 1px 1px rgba(0,0,0,.35);
    box-shadow: 0 1px 2px rgba(0,0,0,.3);
  }
  .size-label {
    position: absolute;
    font-size: 20px;
    color: var(--label);
    transform: translateX(-50%);
  }

  /* Leaderboard 728x90 */
  .leaderboard { left: 135px; top: 122px; width: 933px; height: 113px; }
  .leaderboard .band-sky { left: 0; top: 0; width: 353px; height: 100%; }
  .leaderboard .band-leaf-v { left: 353px; top: 0; width: 10px; height: 100%; }
  .leaderboard .headline {
    left: 0; width: 353px; top: 24px;
    font-size: 28px; line-height: 32px; text-align: center;
  }
  .leaderboard .tagline {
    left: 363px; width: 240px; top: 9px;
    font-size: 22px; line-height: 23px; text-align: center;
  }
  .leaderboard .portrait { left: 603px; top: 0; width: 130px; height: 100%; }
  .leaderboard .band-night { left: 733px; top: 0; width: 200px; height: 100%; }
  .leaderboard .cta { left: 761px; top: 34px; }

  /* Medium rectangle 300x250 */
  .rectangle { left: 135px; top: 328px; width: 384px; height: 320px; }
  .rectangle .band-sky { left: 0; top: 0; width: 100%; height: 127px; }
  .rectangle .band-leaf-h { left: 0; top: 127px; width: 100%; height: 11px; }
  .rectangle .headline {
    left: 17px; top: 12px;
    font-size: 29px; line-height: 33px;
  }
  .rectangle .tagline {
    left: 17px; top: 161px;
    font-size: 21px; line-height: 21px;
  }
  .rectangle .band-night { left: 0; bottom: 0; width: 100%; height: 63px; }
  .rectangle .portrait { left: 224px; top: 8px; width: 160px; height: 312px; }
  .rectangle .cta { left: 20px; top: 267px; }

  /* Wide skyscraper 160x600 */
  .skyscraper { left: 849px; top: 330px; width: 205px; height: 770px; }
  .skyscraper .band-sky { left: 0; top: 0; width: 100%; height: 264px; }
  .skyscraper .band-leaf-h { left: 0; top: 264px; width: 100%; height: 14px; }
  .skyscraper .headline {
    left: 0; top: 18px; width: 100%;
    font-size: 33px; line-height: 36px; text-align: center;
  }
  .skyscraper .tagline {
    left: 0; top: 296px; width: 100%;
    font-size: 20px; line-height: 21px; text-align: center;
  }
  .skyscraper .portrait { left: 0; top: 389px; width: 100%; height: 302px; }
  .skyscraper .band-night { left: 0; bottom: 0; width: 100%; height: 80px; }
  .skyscraper .cta { left: 24px; top: 708px; }
</style>
</head>
<body>

  <section class="banner leaderboard" aria-label="728 by 90 leaderboard ad">
    <div class="band-sky"></div>
    <div class="band-leaf-v"></div>
    <h2 class="headline">Invest in Real Estate<br>like a PRO</h2>
    <p class="tagline">Brody Halvaney<br>#1 Real Estate<br>investing<br>Strategy</p>
    <div class="portrait" role="img" aria-label="Portrait photo of the presenter in a grey suit jacket"></div>
    <div class="band-night"></div>
    <div class="cta">Get Started</div>
  </section>
  <span class="size-label" style="left:612px; top:245px;">728X90</span>

  <section class="banner rectangle" aria-label="300 by 250 medium rectangle ad">
    <div class="band-sky"></div>
    <div class="band-leaf-h"></div>
    <div class="band-night"></div>
    <div class="portrait" role="img" aria-label="Portrait photo of the presenter in a grey suit jacket"></div>
    <h2 class="headline">Invest In Real<br>Estate Like<br>a PRO</h2>
    <p class="tagline">Brody Halvaney<br>#1 Real Estate<br>investing Strategy</p>
    <div class="cta">Get Started</div>
  </section>
  <span class="size-label" style="left:237px; top:695px;">300X250</span>

  <section class="banner skyscraper" aria-label="160 by 600 skyscraper ad">
    <div class="band-sky"></div>
    <div class="band-leaf-h"></div>
    <h2 class="headline">Invest<br>In<br>Real<br>Estate<br>Like<br>a PRO</h2>
    <p class="tagline">Brody Halvaney #1<br>Real Estate<br>Investing<br>Strategy</p>
    <div class="portrait" role="img" aria-label="Portrait photo of the presenter in a grey suit jacket"></div>
    <div class="band-night"></div>
    <div class="cta">Get Started</div>
  </section>
  <span class="size-label" style="left:947px; top:1106px;">160X600</span>

</body>
</html>
```